Wedding dance company needs flyer design

I am looking for a double sided A5 flyer to be designed for my company Step Quill.

The concept of the flyer is to attract couples for their first wedding dance.

This is to support content of our website: http://www.stepquillgroup.example/bridal-set

All the text content for the flyer is attached in flyer.txt. My company logo is attached in logo.zip.

I would like to have 1-2 photos on the flyer based on a couple and their wedding first dance and perhaps some designs without photos (graphics instead).

```html
<!DOCTYPE html>
<html lang="en">
<head>
<meta charset="utf-8">
<title>Step Quill – First Dance Flyer</title>
<link rel="stylesheet" href="https://fonts.googleapis.com/css2?family=Exo:wght@500;600&family=Arimo:ital,wght@0,400;1,700&display=swap">
<style>
  :root {
    --pink: #e61e8c;
    --pink-soft: #f08cbf;
    --pink-pale: #f7c4dd;
    --green: #9ccd2a;
    --green-soft: rgba(170, 215, 140, .55);
    --green-faint: rgba(200, 232, 185, .35);
    --mint: #eef6f1;
    --ink: #222222;
    --white: #ffffff;
    --backdrop: #ececec;
  }
  * { margin: 0; padding: 0; box-sizing: border-box; }
  html, body { width: 1200px; height: 1000px; overflow: hidden; }
  body { background: var(--backdrop); position: relative; }

  .flyer {
    position: absolute; top: 97px; width: 570px; height: 806px;
    background: var(--white); overflow: hidden;
    box-shadow: 0 4px 18px rgba(0,0,0,.18);
  }
  .flyer--front { left: 20px; }
  .flyer--back { left: 610px; }

  .wash { position: absolute; pointer-events: none; }
  .wash--front-top {
    right: 0; top: 0; width: 420px; height: 380px;
    background: radial-gradient(ellipse at 75% 55%, var(--green-soft) 0%, var(--green-faint) 45%, rgba(255,255,255,0) 75%);
  }
  .wash--front-bottom {
    right: 0; bottom: 0; width: 300px; height: 220px;
    background: radial-gradient(ellipse at 90% 80%, var(--green-soft) 0%, rgba(255,255,255,0) 70%);
  }
  .wash--back-bottom {
    right: 0; bottom: 0; width: 320px; height: 230px;
    background: radial-gradient(ellipse at 90% 85%, var(--green-soft) 0%, rgba(255,255,255,0) 70%);
  }

  .brand {
    position: absolute; font-family: "Exo", sans-serif; font-weight: 600;
    color: var(--pink); display: flex; align-items: center; gap: 10px; line-height: 1;
  }
  .brand__mark { width: 12px; height: 12px; background: var(--green); }
  .flyer--front .brand { top: 40px; right: 34px; font-size: 46px; }

  .couple-art {
    position: absolute; left: 20px; top: 150px; width: 300px; height: 440px;
    border-radius: 14px;
    background: linear-gradient(160deg, var(--pink-soft) 0%, var(--pink-pale) 55%, var(--white) 100%);
  }

  .headline { position: absolute; top: 290px; right: 0; font-family: "Exo", sans-serif; font-weight: 500; }
  .headline__line {
    display: block; width: max-content; margin-left: auto; margin-bottom: 12px;
    background: var(--pink); color: var(--white);
    font-size: 36px; font-weight: 500; line-height: 1; padding: 8px 14px 10px;
  }
  .headline__line:nth-child(1) { margin-right: 14px; }
  .headline__line:nth-child(2) { margin-right: 20px; }
  .headline__line:nth-child(3) { margin-right: 32px; }
  .headline__line:nth-child(4) { margin-right: 36px; }

  .call-out {
    position: absolute; left: 30px; top: 636px; width: 520px;
    font-family: "Exo", sans-serif; font-weight: 600; font-size: 38px;
    line-height: 1.2; color: var(--pink);
  }
  .call-out__line { display: block; white-space: nowrap; }
  .call-out__name { color: var(--green); }

  .intro {
    position: absolute; left: 20px; top: 20px; width: 530px; height: 330px;
    background: var(--mint); padding: 22px 24px;
    font-family: "Arimo", sans-serif; font-size: 15.5px; line-height: 1.38; color: var(--ink);
    text-align: justify;
  }
  .intro p { margin-bottom: 12px; }

  .packages {
    position: absolute; left: 0; top: 368px; width: 100%; height: 250px;
    background: var(--pink-soft); color: var(--white);
    font-family: "Arimo", sans-serif; font-style: italic; font-weight: 700;
    padding: 24px 30px;
  }
  .packages__title { font-size: 17px; margin-bottom: 18px; }
  .packages__list { list-style: none; font-size: 19px; line-height: 1.5; }
  .packages__list .indent { padding-left: 210px; display: block; }

  .extras {
    position: absolute; left: 30px; top: 636px; width: 510px;
    font-family: "Arimo", sans-serif; font-size: 15px; line-height: 1.35; color: var(--ink);
    text-align: right;
  }

  .contacts {
    position: absolute; right: 26px; top: 692px; list-style: none;
    font-family: "Arimo", sans-serif; font-size: 13.5px; color: var(--ink);
  }
  .contacts li { display: flex; align-items: center; gap: 8px; margin-bottom: 7px; min-height: 16px; }
  .contacts li.no-icon { padding-left: 24px; }
  .contacts svg { width: 16px; height: 16px; flex: none; }

  .flyer--back .brand { left: 30px; top: 724px; font-size: 30px; }
  .site-url {
    position: absolute; left: 30px; top: 766px;
    font-family: "Arimo", sans-serif; font-size: 13px; color: var(--pink);
  }
</style>
</head>
<body>

<section class="flyer flyer--front">
  <div class="wash wash--front-top" role="img" aria-label="Soft green abstract wave backdrop"></div>
  <div class="wash wash--front-bottom" role="img" aria-label="Soft green abstract wave backdrop"></div>

  <div class="brand"><span>Step Quill</span><span class="brand__mark"></span></div>

  <div class="couple-art" role="img" aria-label="Illustration of a bride and groom silhouette sharing their first dance"></div>

  <h1 class="headline">
    <span class="headline__line">Are you feeling</span>
    <span class="headline__line">nervous about</span>
    <span class="headline__line">your first</span>
    <span class="headline__line">dance ?</span>
  </h1>

  <p class="call-out">
    <span class="call-out__line">Then why not let</span>
    <span class="call-out__line"><span class="call-out__name">Step Quill</span> take care of</span>
    <span class="call-out__line">all the planning for you!</span>
  </p>
</section>

<section class="flyer flyer--back">
  <div class="wash wash--back-bottom" role="img" aria-label="Soft green abstract wave backdrop"></div>

  <div class="intro">
    <p>We specialise in preparing couples for their first dance on their wedding day.</p>
    <p>Lessons take place in a studio of your choice or in the comfort of your home. We provide a wide range of dance packages to suit all budgets.</p>
    <p>We are a friendly business, provide flexibility and patience to make sure you feel comfortable and confident on the day. Whether you want simple steps, a classic routine or a full extravaganza, you'll soon be able to wow your guests.</p>
    <p>Your wedding dance will match your song, style and ability, so it will never be too difficult and always fun.</p>
  </div>

  <div class="packages">
    <p class="packages__title">Our packages (starting at £65)</p>
    <ul class="packages__list">
      <li>Basic Package - 1 x 1 hour lesson</li>
      <li>Silver Package - 1 x 90 minute lesson</li>
      <li>Gold Package - 2 x 90 minute lessons</li>
      <li>Platinum Package - 1 x 2 hour lesson and <span class="indent">2 x 90 minute lessons</span></li>
    </ul>
  </div>

  <p class="extras">We also offer the SOS last minute package, wedding rehearsals, hen parties and gift vouchers.</p>

  <ul class="contacts">
    <li>
      <svg viewBox="0 0 16 16" aria-hidden="true"><rect width="16" height="16" fill="#222"/><path d="M4 5c0-1 1-1.5 4-1.5S12 4 12 5v1.5h-2.2V5.5H6.2v1H4Z M5 8h6l1 4H4Z" fill="#fff"/></svg>
      07700 900118 / 07700 900119
    </li>
    <li>
      <svg viewBox="0 0 16 16" aria-hidden="true"><rect width="16" height="16" fill="#e61e8c"/><rect x="3" y="4.5" width="10" height="7" fill="none" stroke="#fff" stroke-width="1.2"/><path d="M3 4.5 8 8.5 13 4.5" fill="none" stroke="#fff" stroke-width="1.2"/></svg>
      info@stepquillgroup.example
    </li>
    <li class="no-icon">facebook.com/stepquillgroupevents</li>
    <li class="no-icon">@StepQuillCo</li>
  </ul>

  <div class="brand"><span>Step Quill</span><span class="brand__mark"></span></div>
  <p class="site-url">www.stepquillgroup.example</p>
</section>

</body>
</html>
```